Unique Flyer Project - www.plumorchardpanel.com.au

The purpose of this flyer is trying to get recipients to visit the website www.plumorchardpanel.com.au and sign up to the offer. I need it to be simple/to the point, eye catching and professional. I will post up a basic idea I have but feel free to put your own spin on it if you think you have great ideas to get people to visit the site, if not then just improve upon the quality of mine and make it look like a respected company.

I also think a red band or something that REALLY catches the eye highlighting one of the important aspects of the flyer (the domain?) could be great so even if someone is about to put it in the bin, the popping red-on-white-background catches their eye so they end up looking at and reading the flyer.

I would also love a VERY SIMPLE design for the backside of the flyer, just a red box/band (whatever you think is good) with the domain 'www.plumorchardpanel.com.au' in it. NOTHING ELSE! Just so if it's floating around the table and it's upside down, there's something eye catching that might entice the householder to look at it.

DESIGN IS FOR DL FLYER: 99mm X 210mm

Target Market(s)

Australian Residents interested in earning money from home.

Industry/Entity Type

It Company

Requirements
Must have
• Eye catching (mainly red band/box/bar on front & back page), SIMPLE, elegant/professional.
Should not have
• ANYTHING unnecessary to the reader that will distract them from the ultimate point - GET PAID TO DO SURVEYS FROM YOUR OWN HOME ON THE COMPUTER!

```html
<!DOCTYPE html>
<html lang="en">
<head>
<meta charset="utf-8">
<title>Plum Orchard Panel – DL Flyer</title>
<link rel="stylesheet" href="https://fonts.googleapis.com/css2?family=Oswald:wght@400;500;600;700&display=swap">
<style>
  :root {
    --page-bg: #8a8a8a;
    --paper: #f1f1f1;
    --ink: #1c1c1c;
    --brand-blue: #1478b8;
    --brand-blue-dark: #0d5f96;
    --band-red: #d8301f;
    --band-red-dark: #b21f12;
    --white: #ffffff;
    --photo-tone: #c9452c;
    --flag-tone: #2a3f8f;
  }
  * { box-sizing: border-box; margin: 0; padding: 0; }
  html, body {
    width: 1200px; height: 720px; overflow: hidden;
    background: var(--page-bg);
    font-family: "Oswald", "Arial Narrow", sans-serif;
  }
  .canvas {
    width: 1200px; height: 720px;
    display: flex; flex-direction: column; align-items: center; justify-content: center;
    gap: 24px;
  }
  .flyer {
    position: relative;
    width: 700px; height: 330px;
    background: var(--paper);
    overflow: hidden;
    box-shadow: 0 6px 18px rgba(0,0,0,.25);
  }

  /* Shared red domain band */
  .domain-band {
    position: absolute;
    height: 58px;
    background: linear-gradient(180deg, var(--band-red), var(--band-red-dark));
    border-radius: 6px;
    display: flex; align-items: center; justify-content: center;
    color: var(--white);
    font-weight: 500;
    font-size: 25px;
    letter-spacing: 3.5px;
    text-transform: uppercase;
  }
  .domain-band .cursor {
    position: absolute; right: -8px; bottom: -14px;
    width: 20px; height: 26px;
  }

  /* Back side */
  .flyer-back .domain-band { left: 70px; right: 70px; top: 80px; }

  /* Front side */
  .offer-burst { position: absolute; left: 0; top: 0; width: 280px; height: 330px; }
  .offer-copy {
    position: absolute; left: 0; top: 42px; width: 240px;
    text-align: center; color: var(--white); text-transform: uppercase;
    line-height: 1;
  }
  .offer-copy .earn { font-size: 58px; font-weight: 600; }
  .offer-copy .as-much { font-size: 24px; font-weight: 500; margin-top: 4px; }
  .offer-copy .amount { font-size: 104px; font-weight: 600; margin-top: 2px; }
  .offer-copy .per-survey { font-size: 27px; font-weight: 500; margin-top: 6px; }

  .brand-row {
    position: absolute; left: 275px; top: 24px; width: 405px; height: 86px;
    display: flex; align-items: center; gap: 12px;
  }
  .brand-name {
    font-size: 30px; font-weight: 700; line-height: 1.02;
    color: var(--brand-blue); text-transform: uppercase;
    width: 180px;
  }
  .brand-photo {
    width: 100px; height: 72px; border-radius: 4px;
    background: linear-gradient(135deg, var(--photo-tone), #7a5040);
  }
  .region-note { margin-left: auto; width: 78px; text-align: center; color: var(--ink); }
  .region-flag {
    width: 70px; height: 40px; margin: 0 auto 4px;
    background: linear-gradient(135deg, var(--flag-tone), #1d2c66);
    border: 1px solid #999;
  }
  .region-note .small { font-size: 9px; font-weight: 400; line-height: 1.15; display: block; }
  .region-note .country { font-size: 11px; font-weight: 500; text-transform: uppercase; }

  .headline {
    position: absolute; left: 275px; top: 130px; width: 410px;
    font-size: 27px; font-weight: 600; color: var(--ink); text-transform: uppercase;
  }
  .subline {
    position: absolute; left: 275px; top: 170px; width: 410px;
    font-size: 20px; font-weight: 400; color: var(--ink);
  }
  .flyer-front .domain-band { left: 268px; right: 22px; top: 236px; font-size: 23px; letter-spacing: 3px; }
</style>
</head>
<body>
<main class="canvas">

  <section class="flyer flyer-back" aria-label="Flyer back">
    <div class="domain-band">www.plumorchardpanel.com.au
      <svg class="cursor" viewBox="0 0 20 26" aria-hidden="true"><path d="M2 2 L2 21 L7 16 L11 24 L14 22.5 L10 15 L17 15 Z" fill="#000" stroke="#fff" stroke-width="1.5" stroke-linejoin="round"/></svg>
    </div>
  </section>

  <section class="flyer flyer-front" aria-label="Flyer front">
    <svg class="offer-burst" viewBox="0 0 280 330" aria-hidden="true">
      <defs>
        <linearGradient id="burstFill" x1="0" y1="0" x2="1" y2="1">
          <stop offset="0" stop-color="#1a84c6"/>
          <stop offset="1" stop-color="#0d5f96"/>
        </linearGradient>
      </defs>
      <polygon fill="url(#burstFill)" stroke="#1272b0" stroke-width="14" stroke-linejoin="round"
        points="275,165 253,201 254,243 218,263 198,299 156,298 120,320 84,298 42,299 22,263 -14,243 -13,201 -35,165 -13,129 -14,87 22,67 42,31 84,32 120,10 156,32 198,31 218,67 254,87 253,129"/>
    </svg>
    <div class="offer-copy">
      <div class="earn">Earn</div>
      <div class="as-much">as much as</div>
      <div class="amount">$50</div>
      <div class="per-survey">per survey!</div>
    </div>

    <div class="brand-row">
      <div class="brand-name">Plum Orchard Panel</div>
      <div class="brand-photo" role="img" aria-label="Photo of a person taking a survey on a laptop"></div>
      <div class="region-note">
        <div class="region-flag" role="img" aria-label="Australian flag"></div>
        <span class="small">Now open to<br>Residents of</span>
        <span class="country">Australia</span>
      </div>
    </div>

    <h1 class="headline">Could you use an extra income?</h1>
    <p class="subline">Work from home and choose your own hours!</p>

    <div class="domain-band">www.plumorchardpanel.com.au
      <svg class="cursor" viewBox="0 0 20 26" aria-hidden="true"><path d="M2 2 L2 21 L7 16 L11 24 L14 22.5 L10 15 L17 15 Z" fill="#000" stroke="#fff" stroke-width="1.5" stroke-linejoin="round"/></svg>
    </div>
  </section>

</main>
</body>
</html>
```